We are a printed circuit board manufacturer. Need a company professional web site to allow our potential customers to know more about our background, capability and our products. The web site will contain three languages, which are Chinese, English and Japanese. Our audience are mainly electronic companies that procure printed circuit boards. I have a word document that have all the required text in all three languages. The final design should communicate the impression that we embrace quality, trustworthiness and long term partnership business principles.
We should have sections that allow us to post pictures of our facilities.
I have added the three files in three different languages.
Some of the information is below:
Background
RVD Worldwide Limited (RVD) was set up in Hong Kong in 2007 by two Hong Kong entrepreneurs, Mr. Lok Fai Tam and Mr. Wai Ho. We acquired the single sided printed circuit board factory located in Dongguan City, Guangdong Province, China, from Valtor Corporation of the U.S. in 2007. In addition to RVD, Mr. Tam and Mr. Ho also own Brightrail Systems Company Limited, a semiconductor company based in Hong Kong since 1997 with a total investment of over US$100 million. Brightrail is engaged in the manufacturing of flexible substrates and MEMS assembly business.
RVD has been awarded TS 16949 and ISO14000 certificates since 2009 and 2004 respectively.
Business Principles
RVD Worldwide Limited strives to be a professional top notched printed circuit board supplier. We embrace four “EXCELLENCE” principles, namely, excellence in quality, excellence in prices, excellence in services and excellence in on time delivery.
We approach each customer with a long-term partnership view that delivers the lowest ownership costs and highest total values to our customers. We customize quotations and solutions in order to allow our customers to win more businesses. We believe by thinking from our customers’ points of view we will be able to create a WIN-WIN relationship.
Customers
Due to our excellent quality, services and production systems, RVD Worldwide Limited manage to service a number of large Japanese and US customers, which include:
Technical capability overview
Below is an overview of our current capability:
Target Market(s)
Electronic companies buyers
Industry/Entity Type
Business
Requirements
Must have
- Capability description
Should not have
- no cartoon

```html
<!DOCTYPE html>
<html lang="en">
<head>
<meta charset="utf-8">
<title>RVD Worldwide Limited</title>
<link rel="stylesheet" href="https://fonts.googleapis.com/css2?family=Bree+Serif&family=Carlito:wght@400;700&family=Open+Sans:ital,wght@0,400;0,600;0,700;1,400&display=swap">
<style>
:root{
  --green:#0f6a45;
  --green-dark:#0d4f33;
  --green-text:#1f7a55;
  --red:#d3362b;
  --blue-top:#5a8fd0;
  --blue-bot:#2d5fa5;
  --text:#444;
  --muted:#666;
  --gray-panel:#e6e6e6;
  --gray-head:#5f5f5f;
  --gold:#f2b500;
  --foot-link:#79c9a0;
  --foot-yellow:#f7c325;
}
*{box-sizing:border-box;margin:0;padding:0}
html,body{width:820px;height:1200px;overflow:hidden}
body{position:relative;background:#fff;font-family:"Open Sans",Arial,sans-serif;color:var(--text)}
.abs{position:absolute}
.page-top{left:0;top:0;width:820px;height:290px;background:linear-gradient(#fff 0,#f4f6f5 120px,#dfe7e3 200px,#7aa894 245px,#2f6e55 290px)}
.logo{left:96px;top:14px;width:115px;text-align:center;color:var(--green);font-family:"Carlito",sans-serif;font-weight:700;line-height:1}
.logo-mark{font-size:27px;letter-spacing:2px}
.logo-sub{font-size:10px;margin-top:1px}
.lang{left:461px;top:19px;font-size:8px;color:#222;font-weight:600;display:flex;align-items:center;gap:4px}
.lang-select{width:56px;height:12px;border-radius:6px;background:linear-gradient(#fff,#ccc);border:1px solid #999;font-size:7px;font-weight:400;padding-left:4px;position:relative;line-height:10px}
.lang-select::after{content:"";position:absolute;right:0;top:0;width:13px;height:10px;border-radius:0 6px 6px 0;background:#2e8b57}
.call{left:606px;top:16px;font-size:9px;font-weight:700;color:#222}
.call-phone{display:block;font-size:17px;font-weight:400;color:var(--red);margin-top:3px}
.nav{left:96px;top:69px;width:628px;height:28px;border-radius:7px 7px 0 0;background:linear-gradient(var(--blue-top),var(--blue-bot));display:flex}
.nav a{color:#fff;text-decoration:none;font-size:10px;line-height:28px;text-align:center;border-right:1px solid #6d98cf}
.nav a:last-child{border:0}
.hero{left:96px;top:97px;width:628px;height:211px;background:linear-gradient(90deg,#eef0f2,#fafbfc);border-radius:0 0 7px 7px;overflow:hidden;border:1px solid #c9d3dc;border-top:0}
.hero svg{position:absolute;left:0;top:0}
.hero-caption{left:0;top:180px;width:380px;height:31px;background:rgba(40,55,70,.75);color:#fff;font-family:Arial,sans-serif;font-weight:700;font-size:17px;line-height:31px;padding-left:20px}
.hero-title{right:14px;top:40px;text-align:right;font-family:"Bree Serif",serif;font-size:17px;line-height:20px;color:#333;font-weight:400}
.hero-title em{font-style:normal;color:var(--red)}
.hero-text{right:14px;top:101px;width:230px;text-align:right;font-size:9px;line-height:14px;color:#333}
.hero-btn{left:454px;top:163px;width:107px;height:22px;border-radius:3px;background:linear-gradient(#f7cf3c,#e3a100);border:1px solid #c28a00;font-size:10px;line-height:20px;text-align:center;color:#333}
.h2{font-family:"Carlito",sans-serif;font-size:16px;color:#222;font-weight:400}
.h2 span{color:var(--red)}
.copy{font-size:7.7px;line-height:15.5px;color:var(--text);letter-spacing:-0.05px}
.more{font-size:8px;font-style:italic;color:var(--red)}
.more::before{content:"» ";font-style:normal}
.rule{height:1px;width:426px;left:96px;background:linear-gradient(90deg,transparent,#ccc,transparent)}
.thumb{border:1px solid #ccc;padding:3px;background:#fff;box-shadow:0 1px 2px rgba(0,0,0,.15)}
.thumb div{width:100%;height:100%}
.products{left:96px;top:667px;width:426px;height:165px;background:#f0f0f0;border-radius:4px}
.product-title{font-family:"Carlito",sans-serif;font-size:11.5px;color:var(--green-text);white-space:nowrap}
.clients{left:96px;top:872px;width:426px;height:83px;background:linear-gradient(#fff,#eee);border:1px solid #ddd;box-shadow:0 6px 8px -6px rgba(0,0,0,.35)}
.client{top:13px;width:67px;height:57px;background:#fff;border:1px solid #ccc;box-shadow:0 1px 3px rgba(0,0,0,.2);display:flex;align-items:center;justify-content:center;font-family:"Open Sans",sans-serif;font-weight:700;font-size:11px;color:#333}
.side{left:559px;width:165px;background:var(--gray-panel);border-bottom:2px solid #f0c58a}
.side-head{height:26px;font-family:"Carlito",sans-serif;font-size:15px;color:#fff;line-height:26px;padding-left:13px;background:linear-gradient(#777,#555)}
.side-head.green{background:linear-gradient(#168a5a,#0b6340)}
.cap-list{list-style:none;padding:3px 10px 0 10px}
.cap-list li{font-size:8.5px;color:#222;height:23px;line-height:23px;border-bottom:1px solid #d6d6d6;padding-left:11px;position:relative}
.cap-list li:last-child{border:0}
.cap-list li::before{content:"";position:absolute;left:1px;top:10px;width:3px;height:3px;background:#555}
.bubble{left:7px;top:34px;width:151px;height:104px;background:#fff;border-radius:12px;box-shadow:0 1px 3px rgba(0,0,0,.25);font-size:8.2px;font-style:italic;line-height:14px;color:#444;padding:16px 10px 0 13px}
.bubble::after{content:"";position:absolute;left:22px;bottom:-10px;border:6px solid transparent;border-top:6px solid #fff;border-left:6px solid #fff}
.blog-item{left:13px;width:150px}
.blog-item b{display:block;font-weight:400;color:var(--red);font-size:9.5px;padding-left:14px;line-height:12px;white-space:nowrap}
.blog-item p{font-size:8px;line-height:14px;color:#444;padding-left:14px}
.blog-item svg{position:absolute;left:0;top:1px}
.view-all{left:108px;top:192px;width:45px;height:18px;border-radius:3px;background:linear-gradient(#4a7fc4,#1f4f91);color:#fff;font-size:8.5px;font-weight:600;line-height:18px;text-align:center}
.footer{left:0;top:975px;width:820px;height:225px;background:linear-gradient(#0f5a3b,#0d4d33);color:#fff}
.f-head{font-family:"Carlito",sans-serif;font-size:16px;color:#fff;font-weight:400}
.f-sub{font-size:8.5px;font-weight:600;color:#fff}
.f-line{font-size:7.5px;line-height:14px;color:var(--foot-link)}
.f-contact{font-size:9px;color:#fff;line-height:19px}
.f-contact .big{color:var(--foot-yellow);font-size:13px;margin-left:4px}
.f-contact u{color:#fff;margin-left:2px}
.links{list-style:none}
.links li{font-size:7.5px;line-height:15.3px;color:var(--foot-link)}
.social{left:614px;width:110px;height:25px;background:rgba(255,255,255,.09);border-radius:3px;font-size:7.5px;color:var(--foot-link);display:flex;align-items:center;padding-left:7px;gap:7px;white-space:nowrap}
.social i{display:block;width:19px;height:19px;border-radius:2px;flex:none}
.copyright{left:96px;top:1177px;font-size:8.5px;color:var(--foot-link)}
</style>
</head>
<body>
<div class="abs page-top"></div>

<header>
  <div class="abs logo"><div class="logo-mark">RVD</div><div class="logo-sub">Worldwide Limited</div></div>
  <div class="abs lang">Select Language: <span class="lang-select">English</span></div>
  <div class="abs call">Call Us Now!<span class="call-phone">(852)24608190</span></div>
  <nav class="abs nav">
    <a style="width:67px">Home</a>
    <a style="width:81px">About us</a>
    <a style="width:80px">Products</a>
    <a style="width:78px">Services</a>
    <a style="width:127px">Technical capability</a>
    <a style="width:104px">Infrastructure</a>
    <a style="width:91px">Our Clients</a>
  </nav>
</header>

<section class="abs hero">
  <svg width="400" height="211" role="img" aria-label="Circuit board traces surrounding a view of the earth">
    <defs>
      <linearGradient id="heroFill" x1="0" y1="0" x2="1" y2="0.3">
        <stop offset="0" stop-color="#e0771a"/>
        <stop offset="0.35" stop-color="#d9c24a"/>
        <stop offset="0.55" stop-color="#4f6d8c"/>
        <stop offset="0.8" stop-color="#e8a03a"/>
        <stop offset="1" stop-color="#c9652a"/>
      </linearGradient>
    </defs>
    <polygon points="0,0 344,0 384,211 0,211" fill="url(#heroFill)"/>
    <line x1="344" y1="0" x2="384" y2="211" stroke="#ef7a1e" stroke-width="2"/>
  </svg>
  <div class="abs hero-caption">Lorem ipsum dolor sit amet...</div>
  <h1 class="abs hero-title"><em>Neque porro</em> quisquam est<br>dolorem ipsum dolor sit amet...</h1>
  <p class="abs hero-text">Neque porro quisquam est qui dolorem ipsum quia dolor sit amet, consectetur, adipisci velit there is no one who loves pain itself.</p>
  <div class="abs hero-btn">Click for Capability</div>
</section>

<main>
  <h2 class="abs h2" style="left:96px;top:324px">Welcome to <span>RVD Worldwide Limited</span></h2>
  <div class="abs copy" style="left:96px;top:347px;width:428px">
    <p>Lorem Ipsum is simply dummy text of the printing and typesetting industry. Lorem Ipsum has been the industry's for on standard dummy text ever since the 1500s, when an unknown printer took a galley of type and scrambled it to make a passages, and more recently with desktop publishing.</p>
    <p style="margin-top:5px">Lorem Ipsum is simply dummy text of the printing and typesetting industry. Lorem Ipsum has been the industry's into standard dummy text ever since the 1500s, when an unknown printer took a galley of type and scrambled it to make a type specimen book. It has survived not only five centuries, but also the leap into electronic typesetting, remain go essentially unchanged. It was popularised in the 1960s with the release of Letraset sheets containing lorem Ipsum play type specimen book. It has survived not only five centuries, but also the leap into electronic typesetting.</p>
  </div>
  <div class="abs more" style="left:474px;top:484px">Read More</div>
  <div class="abs rule" style="top:505px"></div>

  <h2 class="abs h2" style="left:96px;top:516px">Our Services</h2>
  <div class="abs thumb" style="left:96px;top:543px;width:79px;height:53px"><div role="img" aria-label="Technician assembling a circuit board" style="background:linear-gradient(135deg,#8fa9c2,#3f6a8e 60%,#c44a3a)"></div></div>
  <p class="abs copy" style="left:187px;top:539px;width:335px">Lorem Ipsum is simply dummy text of the printing and typesetting industry. Lorem Ipsum has been the industry's for on standard dummy text ever since the 1500s, when an unknown printer took a galley of type and scrambled it to make a passages, and more recently with desktop publishing centuries.</p>
  <div class="abs more" style="left:474px;top:607px">Read More</div>
  <div class="abs rule" style="top:628px"></div>

  <h2 class="abs h2" style="left:95px;top:639px">Products</h2>
  <div class="abs products">
    <div class="abs thumb" style="left:6px;top:6px;width:201px;height:92px;padding:7px"><div role="img" aria-label="Single layered printed circuit board with chip" style="background:linear-gradient(135deg,#2f7a4a,#1d4f36 50%,#6a8f5a)"></div></div>
    <div class="abs thumb" style="left:220px;top:6px;width:201px;height:92px;padding:7px"><div role="img" aria-label="Double and multi layered printed circuit board" style="background:linear-gradient(135deg,#3a8a5a,#1f5a3c 55%,#4f8a63)"></div></div>
    <div class="abs product-title" style="left:6px;top:111px">Singal layered printed circuit board</div>
    <div class="abs product-title" style="left:216px;top:111px">Double &amp; Multi layered printed circuit board</div>
    <p class="abs copy" style="left:6px;top:130px;width:205px">Lorem Ipsum is simply dummy text of the printing and typesetting industry standard dummy text.</p>
    <p class="abs copy" style="left:216px;top:130px;width:205px">Lorem Ipsum is simply dummy text of the printing and typesetting industry standard dummy text.</p>
  </div>

  <h2 class="abs h2" style="left:96px;top:845px">Our Client</h2>
  <div class="abs clients">
    <div class="abs client" style="left:12px">Kestrel</div>
    <div class="abs client" style="left:92px">Shoran</div>
    <div class="abs client" style="left:175px">Hikaru</div>
    <div class="abs client" style="left:262px">Arvec</div>
    <div class="abs client" style="left:345px">Borsen</div>
  </div>
</main>

<aside>
  <section class="abs side" style="top:328px;height:197px">
    <div class="side-head green">Technical capability</div>
    <ul class="cap-list">
      <li>Raw Materials</li><li>Plating</li><li>Printing Processes</li><li>Punching And CNC Process</li><li>Depth Tolerance</li><li>Surface Finishing</li><li>Specification for carbon</li>
    </ul>
  </section>

  <section class="abs side" style="top:539px;height:181px">
    <div class="side-head">Client Testimonials</div>
    <div class="abs bubble">Lorem Ipsum is simply dummy text of the printing and type-setting into industry lorem ipsum has been the industry's for on standard...</div>
    <div class="abs" style="left:6px;top:157px;font-size:8.5px;color:var(--red)">Dana Whitfield</div>
  </section>

  <section class="abs side" style="top:734px;height:224px">
    <div class="side-head">Latest Blog</div>
    <div class="abs blog-item" style="top:36px"><svg width="11" height="10"><path d="M1 1h9v6H5l-3 2V7H1z" fill="#fff" stroke="#888"/></svg><b>Neque porro est ipsum quia</b><p>Lorem Ipsum is simply dummy text of the printing and dummy text.</p></div>
    <div class="abs blog-item" style="top:84px"><svg width="11" height="10"><path d="M1 1h9v6H5l-3 2V7H1z" fill="#fff" stroke="#888"/></svg><b>Neque porro est ipsum quia</b><p>Lorem Ipsum is simply dummy text of the printing and dummy text.</p></div>
    <div class="abs blog-item" style="top:132px"><svg width="11" height="10"><path d="M1 1h9v6H5l-3 2V7H1z" fill="#fff" stroke="#888"/></svg><b>Neque porro est ipsum quia</b><p>Lorem Ipsum is simply dummy text of the printing and dummy text.</p></div>
    <div class="abs view-all">View All</div>
  </section>
</aside>

<footer class="abs footer">
  <h3 class="abs f-head" style="left:96px;top:22px">Contact</h3>
  <div class="abs" style="left:96px;top:55px">
    <div class="f-sub">Hong Kong Business Office</div>
    <div class="f-line" style="margin-top:2px">RVD Worldwide Limited<br>28/F Harbour Crest Tower<br>51 Kestrel Road</div>
    <div class="f-contact">Email: <u>Sales@rvdboard.com</u><br>Phone: <span class="big">(852)24608190</span><br>Fax: <span class="big">(852)24608191</span></div>
  </div>
  <div class="abs" style="left:259px;top:55px">
    <div class="f-sub">China Factory</div>
    <div class="f-line" style="margin-top:2px">RVD Worldwide (Dongguan) Limited<br>7 Lianfeng East 3 Road<br>204 Industrial District<br>Qingshan Town, Dongguan<br>Guangdong Province, China 523905</div>
    <div class="f-contact" style="margin-top:2px">Phone: <span class="big">(86)769-845502716</span><br>Fax: <span class="big">(86)769-84550272</span></div>
  </div>
  <h3 class="abs f-head" style="left:486px;top:22px">Quick Links</h3>
  <ul class="abs links" style="left:486px;top:55px">
    <li>Home</li><li>About Us</li><li>Products</li><li>Services</li><li>Technical Capability</li><li>Infrastructure</li><li>Our Clients</li>
  </ul>
  <h3 class="abs f-head" style="left:613px;top:22px">Follow Us</h3>
  <div class="abs social" style="top:59px"><i style="background:#3b5b9a"></i>Follow on Circlebook</div>
  <div class="abs social" style="top:97px"><i style="background:#3aa7dd"></i>Quick talk on Chirper</div>
  <div class="abs social" style="top:136px"><i style="background:#333"></i>Add with Plusly</div>
</footer>
<div class="abs copyright">© 2012 RVD Worldwide Limited | All Rights Reserved</div>
</body>
</html>
```